web site update

I want to get a better website for a small high end remodeling and construction company
I currently have a web site but you will find that it is not good.
www.quenbrickhall.com
We are a high end construction / remodeling company that has been in business since 2003. We primarily work in the mid peninsula of the bay area. Most of our clientele are very educated captains of industry. This group is still the target client.
I had my logo designed by Mint Easel a few years ago and I do like it, I like the orange and black or orange a blue. I don’t have a lot of content on hand as far as professional photographs.
Number of pages not sure and are open to: design pages vs full function website
I think what I am after is a web presence that will seal the deal as we are getting high referrals from past clients.
Construction
1 page

```html
<!DOCTYPE html>
<html lang="en">
<head>
<meta charset="utf-8">
<title>Quenbrick Hall Remodeling</title>
<link href="https://fonts.googleapis.com/css2?family=Raleway:wght@300;400;600;800&family=Arimo:wght@400&family=Great+Vibes&display=swap" rel="stylesheet">
<style>
  :root {
    --orange: #ff6a13;
    --ink: #1a1a1a;
    --text: #555555;
    --light-bg: #f0f0f0;
    --white: #ffffff;
    --footer-dark: #2e2a26;
  }
  * { margin: 0; padding: 0; box-sizing: border-box; }
  html, body { width: 785px; height: 1200px; overflow: hidden; }
  body { position: relative; background: var(--white); font-family: 'Raleway', sans-serif; color: var(--ink); }

  .hero {
    position: absolute; left: 0; top: 0; width: 785px; height: 443px;
    background:
      radial-gradient(ellipse 90px 200px at 120px 270px, rgba(170,185,205,0.85), rgba(170,185,205,0) 100%),
      radial-gradient(ellipse 80px 70px at 365px 330px, rgba(120,120,125,0.55), rgba(120,120,125,0) 100%),
      radial-gradient(ellipse 260px 110px at 420px 120px, rgba(250,246,238,0.95), rgba(250,246,238,0) 100%),
      radial-gradient(ellipse 160px 150px at 640px 350px, rgba(205,180,145,0.8), rgba(205,180,145,0) 100%),
      radial-gradient(ellipse 70px 220px at 15px 220px, rgba(255,250,235,0.9), rgba(255,250,235,0) 100%),
      linear-gradient(180deg, #efe4d2 0%, #e6d3b6 35%, #c9ad88 62%, #b08d69 85%, #7a5c44 100%);
  }
  .hero-title {
    position: absolute; left: 0; top: 185px; width: 785px; text-align: center;
    font-weight: 800; font-size: 56px; letter-spacing: -1.5px; color: var(--white);
    text-shadow: 0 2px 6px rgba(0,0,0,0.25);
  }

  .site-nav { position: absolute; left: 0; top: 0; width: 785px; height: 48px; }
  .site-nav .rule { position: absolute; top: 48px; height: 1px; background: rgba(255,255,255,0.8); }
  .site-nav a {
    position: absolute; top: 17px; font-size: 12px; color: #2b2b2b; text-decoration: none; letter-spacing: 0.2px;
  }
  .site-nav a.active { color: var(--orange); }
  .brand {
    position: absolute; left: 292px; top: 14px; width: 206px; height: 46px;
    display: flex; align-items: center; justify-content: center; gap: 8px; white-space: nowrap;
  }
  .brand .mark { width: 14px; height: 14px; background: var(--ink); }
  .brand .name { font-weight: 800; font-size: 16px; color: var(--orange); letter-spacing: 0.5px; }

  .welcome { position: absolute; left: 0; top: 443px; width: 785px; height: 300px; background: var(--light-bg); }
  .welcome-copy { position: absolute; left: 50px; top: 47px; width: 328px; text-align: center; }
  .welcome-copy .mark { width: 14px; height: 14px; background: var(--ink); margin: 0 auto; }
  .welcome-copy .script { font-family: 'Great Vibes', cursive; font-size: 15px; margin-top: 2px; color: var(--ink); }
  .welcome-copy h1 { font-weight: 300; font-size: 26px; color: var(--orange); margin-top: 0; letter-spacing: 0.3px; }
  .welcome-copy p { font-family: 'Arimo', sans-serif; font-size: 9.6px; line-height: 15.2px; color: var(--text); margin-top: 8px; }
  .btn {
    display: inline-block; margin-top: 17px; width: 102px; height: 27px; line-height: 27px;
    background: var(--orange); color: var(--white); font-family: 'Arimo', sans-serif; font-size: 11px; text-decoration: none;
  }
  .welcome-photo {
    position: absolute; left: 407px; top: 41px; width: 327px; height: 218px;
    background:
      radial-gradient(ellipse 60px 60px at 165px 80px, rgba(225,150,90,0.75), rgba(225,150,90,0) 100%),
      radial-gradient(ellipse 90px 50px at 255px 150px, rgba(165,155,140,0.7), rgba(165,155,140,0) 100%),
      radial-gradient(ellipse 40px 40px at 290px 115px, rgba(140,175,200,0.6), rgba(140,175,200,0) 100%),
      linear-gradient(180deg, #f4f1ec 0%, #ebe6de 55%, #ddd6ca 75%, #cfc7ba 100%);
  }

  .gallery { position: absolute; left: 0; top: 743px; width: 785px; height: 314px; }
  .gallery h2 {
    position: absolute; left: 0; top: 31px; width: 785px; text-align: center;
    font-weight: 300; font-size: 26px; color: var(--orange);
  }
  .gallery .script {
    position: absolute; left: 0; top: 62px; width: 785px; text-align: center;
    font-family: 'Great Vibes', cursive; font-size: 15px; color: var(--ink);
  }
  .gallery-item { position: absolute; top: 102px; width: 163px; height: 177px; }
  .gallery-item.bath { left: 51px; background: linear-gradient(160deg, #d8d8d4, #a9a8a2); }
  .gallery-item.bedroom {
    left: 224px;
    background:
      radial-gradient(ellipse 60px 30px at 82px 105px, rgba(245,235,210,0.9), rgba(245,235,210,0) 100%),
      linear-gradient(180deg, #d9c59a 0%, #b89563 45%, #7a4a2a 72%, #5e3520 100%);
  }
  .gallery-item.kitchen {
    left: 397px;
    background:
      radial-gradient(ellipse 35px 25px at 120px 75px, rgba(230,220,170,0.9), rgba(230,220,170,0) 100%),
      radial-gradient(ellipse 60px 40px at 60px 150px, rgba(235,235,240,0.7), rgba(235,235,240,0) 100%),
      linear-gradient(180deg, #cfcbb0 0%, #a9a68f 45%, #5f5b50 75%, #3a3732 100%);
  }
  .gallery-item.den {
    left: 570px;
    background:
      radial-gradient(ellipse 40px 55px at 135px 90px, rgba(235,240,240,0.85), rgba(235,240,240,0) 100%),
      radial-gradient(ellipse 30px 30px at 30px 100px, rgba(225,235,240,0.7), rgba(225,235,240,0) 100%),
      linear-gradient(180deg, #c6b49c 0%, #9e8a72 55%, #6e5c4a 100%);
  }
  .gallery-item .overlay {
    position: absolute; left: 6px; top: 6px; right: 6px; bottom: 6px; background: rgba(255,106,19,0.8);
  }

  .site-footer {
    position: absolute; left: 0; top: 1057px; width: 785px; height: 143px;
    background:
      radial-gradient(ellipse 200px 80px at 400px 110px, rgba(95,85,72,0.55), rgba(95,85,72,0) 100%),
      linear-gradient(160deg, #3e3832 0%, var(--footer-dark) 50%, #26231f 100%);
    color: var(--white); font-family: 'Arimo', sans-serif;
  }
  .site-footer h3 { position: absolute; top: 18px; font-family: 'Raleway', sans-serif; font-weight: 400; font-size: 13px; }
  .footer-line { position: absolute; font-size: 9.6px; line-height: 15px; white-space: nowrap; }
  .footer-line svg { position: absolute; left: 0; top: 0; }
  .footer-line.with-icon { padding-left: 20px; }
  .footer-line.link-active { color: var(--orange); }
  .footer-line.wrap { white-space: normal; }
  .newsletter-field {
    position: absolute; left: 398px; top: 82px; width: 129px; height: 33px; background: var(--white);
    color: #9a9a9a; font-style: italic; font-size: 9.6px; line-height: 33px; padding-left: 13px;
  }
  .newsletter-submit {
    position: absolute; left: 527px; top: 82px; width: 34px; height: 33px; background: var(--orange);
  }
  .footer-brand {
    position: absolute; left: 588px; top: 40px; width: 140px; display: flex; align-items: center; gap: 6px; white-space: nowrap;
  }
  .footer-brand .mark { width: 12px; height: 12px; background: var(--white); }
  .footer-brand .name { font-family: 'Raleway', sans-serif; font-weight: 800; font-size: 12.5px; color: var(--orange); }
  .copyright { position: absolute; left: 583px; top: 91px; width: 140px; text-align: center; font-size: 9.6px; line-height: 14px; }
  .copyright .accent { color: var(--orange); }
</style>
</head>
<body>

<section class="hero" role="img" aria-label="Bright modern kitchen with light wood cabinets, stainless refrigerator and range">
  <div class="hero-title">HIGH END LIVING</div>
</section>

<nav class="site-nav">
  <div class="rule" style="left:0;width:286px"></div>
  <div class="rule" style="left:499px;width:286px"></div>
  <a class="active" style="left:90px">HOME</a>
  <a style="left:148px">ABOUT</a>
  <a style="left:211px">SERVICES</a>
  <a style="left:519px">PROJECTS</a>
  <a style="left:604px">GALLERY</a>
  <a style="left:679px">CONTACT</a>
  <div class="brand"><span class="mark"></span><span class="name">QUENBRICK HALL</span></div>
</nav>

<section class="welcome">
  <div class="welcome-copy">
    <div class="mark"></div>
    <div class="script">Welcome to</div>
    <h1>QUENBRICK HALL</h1>
    <p>Lorem Ipsum is simply dummy text of the printing and typesetting industry. Lorem Ipsum has been the industry's standard dummy text ever since the 1500s, when an unknown printer took a galley of type and scrambled it to make a type specimen book. It has survived not only five centuries, but also the leap into electronic typesetting, remaining essentially unchanged.</p>
    <a class="btn">READ MORE</a>
  </div>
  <div class="welcome-photo" role="img" aria-label="Light living room with sofa opening onto a sunroom"></div>
</section>

<section class="gallery">
  <h2>OUR GALLERY</h2>
  <div class="script">Lorem ipsum is simply dummy text of the printing and typesetting</div>
  <div class="gallery-item bath" role="img" aria-label="Tiled shower with chrome fixtures">
    <div class="overlay"></div>
    <svg width="163" height="177" style="position:absolute;left:0;top:0">
      <path d="M64 88.5H100M82 70.5V106.5" stroke="#ffffff" stroke-width="1"/>
    </svg>
  </div>
  <div class="gallery-item bedroom" role="img" aria-label="Bedroom with wooden bed in an arched alcove"></div>
  <div class="gallery-item kitchen" role="img" aria-label="Kitchen with island and white bar stools"></div>
  <div class="gallery-item den" role="img" aria-label="Sunny room with armchair under a vaulted ceiling"></div>
</section>

<footer class="site-footer">
  <h3 style="left:52px">CONTACT INFO</h3>
  <div class="footer-line with-icon" style="left:52px;top:42px">
    <svg width="16" height="14" viewBox="0 0 16 14"><path d="M1 3L5 1L11 3L15 1V11L11 13L5 11L1 13Z M5 1V11 M11 3V13" fill="none" stroke="#fff" stroke-width="1"/></svg>
    123 Building Name, Area,<br>City, Country - Zipcode
  </div>
  <div class="footer-line with-icon" style="left:52px;top:80px">
    <svg width="15" height="14" viewBox="0 0 15 14"><path d="M3 1L5.5 4L4 5.5C5 8 6.5 9.5 9 10.5L10.5 9L13.5 11.5L11.5 13.5C6 13 1.5 8 1 2.5Z" fill="none" stroke="#fff" stroke-width="1"/></svg>
    415.555.0148
  </div>
  <div class="footer-line with-icon" style="left:52px;top:104px">
    <svg width="15" height="13" viewBox="0 0 15 13"><rect x="0.5" y="1.5" width="14" height="10" fill="none" stroke="#fff"/><path d="M0.5 1.5L7.5 7L14.5 1.5" fill="none" stroke="#fff"/></svg>
    office@quenbrickhall.com
  </div>

  <h3 style="left:225px">USEFUL LINKS</h3>
  <div class="footer-line link-active" style="left:225px;top:42px">Privacy Policy</div>
  <div class="footer-line" style="left:225px;top:62px">Terms &amp; Conditions</div>
  <div class="footer-line" style="left:225px;top:82px">Disclaimer</div>

  <h3 style="left:398px">NEWSLETTER</h3>
  <div class="footer-line wrap" style="left:398px;top:42px;width:160px">Subscribe to get news &amp; Updates of our work</div>
  <div class="newsletter-field">E-Mail</div>
  <div class="newsletter-submit">
    <svg width="34" height="33"><path d="M15 13L19 16.5L15 20" fill="none" stroke="#fff" stroke-width="1.5"/></svg>
  </div>

  <div class="footer-brand"><span class="mark"></span><span class="name">QUENBRICK HALL</span></div>
  <div class="copyright">© <span class="accent">QUENBRICK HALL</span> -<br>2016. All Rights Reserved</div>
</footer>

</body>
</html>
```